Baby and Kids e-shop (Russian language is needed)

We need a web design for e-shop of a Russian company based in Moscow. We sell maternity things, baby and kids goods, clothes, toys, furniture, home and decor, etc.
We need the design that will suit to the exhisting logo. It should be simple and comfortable to the consumers. Attractive but not too bright (so that the goods' pictures attract more attention to them instead of the design).
The domain name of the company is lirabeko.ru
Design of the main page should be similar to the idea of cradleway.com All button names of the main page are provided in attached file.
While choosing certain category from the menu, we should see the list of goods to the left and list of brands to the right (example: http://www.karapuz-lavka.ru/?welcome).

We need:
- main page
- page of the catalogue
- page of the certain category from the catalogue
- page with a certain good
- cart page
- payment page
- lira beko club page (banner and text)
- registration page (banner, registration form, text)

Target Market(s)

pregnant women, young moms

Industry/Entity Type

Baby

Requirements
Must have
• The webdesign should be very clear and similar to cradleway.com You can suggest a kind of design similar to kinderhort.de, wiegelein.de.
The web design should clear state that it is targeted on kids goods, but it is a family e-shop as well.
Nice to have
• 1) In general the design shall be the same as provided sample we like. The design of a page with a concrete good should have tabs: 1) about this good, 2) payment, 3) delivery and return, 4) review; like this: http://www.dapperrackshop.com/t-shirts-c4/vornex-classics-k-tee-swirl-t-shirt-p81174
2) we need design of stickers like in shown example above: 5% off (First order) and Free Coupon for X Rubles for every 1000 Rubles spent online
3) instead of Bookmark&share, ask a question, e-mail a friend and add to wish list, we should have "share" (Chatterly, Drugosfera, Nashkrug - short logos, I will send examples), "ask a question", "e-mail a friend" and "add to gift list" (All this information is contained in downloaded files).

```html
<!DOCTYPE html>
<html lang="ru">
<head>
<meta charset="utf-8">
<title>Lira Beko — детский интернет-магазин</title>
<link href="https://fonts.googleapis.com/css2?family=PT+Serif&family=Arimo:wght@400;700&family=Roboto+Condensed:wght@400;700&family=Russo+One&family=Oswald:wght@500&display=swap" rel="stylesheet">
<style>
:root{
  --red:#c8101a;
  --red-dark:#8e0a10;
  --title-red:#a3121b;
  --green:#8cc21e;
  --green-dark:#5f9410;
  --grey-text:#6b6b6b;
  --dark:#222;
  --panel-border:#d6dcc8;
  --card-bg:#efefef;
  --sticker-bg:#2a2f22;
  --sticker-green:#9be024;
  --sticker-link:#29c6f0;
  --orange:#f39a12;
}
*{box-sizing:border-box;margin:0;padding:0}
html,body{width:1200px;height:1171px;overflow:hidden;background:#fff}
body{position:relative;font-family:"Arimo",Arial,sans-serif;color:var(--dark)}
.abs{position:absolute}

.site-title{left:27px;top:26px;font-family:"PT Serif",Georgia,serif;font-weight:400;font-size:26px;line-height:30px;color:var(--title-red)}
.brand{left:30px;top:110px;display:flex;align-items:center;gap:14px}
.brand-dot{width:96px;height:96px;border-radius:50%;background:#e8431f}
.brand-name{font-family:"PT Serif",Georgia,serif;font-size:40px;color:var(--title-red)}

.top-nav{top:28px;right:14px;display:flex;gap:0}
.top-nav a{display:flex;flex-direction:column;align-items:center;text-decoration:none;color:var(--dark);font-weight:700;font-size:13px;padding:0 12px}
.top-nav svg{width:20px;height:20px;margin-bottom:4px}

.auth{left:766px;top:92px;width:177px;height:24px;background:linear-gradient(#9fd332,var(--green-dark));border-radius:2px;color:#fff;font-weight:700;font-size:12px;display:flex;align-items:center;justify-content:center;gap:10px}
.messenger{left:956px;top:89px;display:flex;align-items:center;gap:8px;font-weight:700;font-size:13px;color:var(--red-dark)}
.messenger i{width:26px;height:26px;border-radius:50%;background:#1fa8e2;display:block}
.contacts{right:15px;top:126px;text-align:left;color:var(--grey-text);font-size:16px;line-height:19px}

.cart-line{left:830px;top:208px;font-size:12px;color:var(--grey-text)}
.cart-line b{color:#555}
.buy-btn{left:1082px;top:202px;width:102px;height:27px;background:linear-gradient(#ef2a1c,#b5060c);border-radius:2px;color:#fff;font-weight:700;font-size:12px;display:flex;align-items:center;justify-content:center}
.search{left:833px;top:236px;width:351px;height:32px;border:1px solid #9a9a9a;background:#fff;font-size:12px;color:#777;padding:9px 8px}
.search svg{position:absolute;right:5px;top:3px;width:25px;height:25px}

.main-menu{left:15px;top:281px;width:1170px;height:57px;background:linear-gradient(#e1141d,#b10a12);display:flex}
.main-menu a{color:#fff;text-decoration:none;font-size:15px;line-height:16px;text-align:center;padding:12px 9px 0;border-right:1px solid #9a0b11;height:100%}
.menu-flaps{left:15px;top:338px;width:1170px;height:12px}

.content{left:27px;top:338px;width:1146px;height:840px;border:1px solid var(--panel-border);border-top:none;background:#f7f8f4}

.banner{left:37px;top:354px;width:818px;height:422px;background:#fff;box-shadow:0 0 4px #bbb}
.banner-photo{position:absolute;left:6px;top:5px;width:806px;height:412px;background:linear-gradient(120deg,#6e8a4e 0%,#a9b58a 35%,#8e8fc9 70%,#6a6fc0 100%)}
.banner-headline{position:absolute;left:20px;top:45px;font-family:"Roboto Condensed",Arial,sans-serif}
.banner-headline .hot{font-size:58px;font-weight:700;color:#ff2a10;line-height:58px;text-shadow:1px 1px 0 #fff}
.banner-headline .sub{font-size:56px;font-weight:400;color:#8e0a10;line-height:56px;text-shadow:2px 2px 0 #fff}
.banner-btns{position:absolute;left:20px;top:160px;display:flex;gap:7px}
.banner-btns span{background:linear-gradient(#ff3b1e,#c20a06);color:#fff;font-size:19px;border-radius:4px;padding:5px 30px 6px 12px;position:relative}
.banner-btns span:after{content:"";position:absolute;right:12px;top:12px;border:5px solid transparent;border-left:6px solid #fff}

.sticker{left:866px;width:300px;background:var(--sticker-bg);border:4px solid #fff;box-shadow:0 0 3px #aaa;padding:10px 10px;overflow:hidden}
.sticker h3{font-family:"Russo One",Impact,sans-serif;font-weight:400;font-size:31px;color:#fff;line-height:36px;white-space:nowrap}
.sticker p{font-family:"PT Serif",Georgia,serif;color:var(--sticker-green);font-size:19px;line-height:17px}
.sticker .big{font-size:26px;line-height:28px}
.sticker .link{font-family:"Arimo",Arial,sans-serif;color:var(--sticker-link);font-size:14px;line-height:16px;margin-top:7px}
.subscribe{left:866px;top:625px;width:300px;height:153px;background:#fff;box-shadow:0 0 3px #aaa;padding:6px}
.subscribe-inner{background:#eee;height:100%;padding:14px 14px}
.subscribe h4{font-family:"Oswald",Arial,sans-serif;font-weight:500;font-size:17px;color:#333}
.subscribe .field{margin-top:8px;height:33px;border:1px solid #ccc;background:#fff;font-size:14px;color:#777;padding:8px 10px}
.subscribe .btn{margin-top:10px;width:126px;height:38px;background:linear-gradient(#b5e34a,#6ea914);border:1px solid #5d8f12;font-weight:700;font-size:18px;color:#222;display:flex;align-items:center;justify-content:center}

.dots{left:367px;top:789px;display:flex;gap:9px}
.dots i{width:14px;height:14px;border-radius:50%;background:var(--orange);display:block}
.dots i.on{background:var(--red)}

.card{top:818px;width:367px;height:360px;background:var(--card-bg);border:1px solid #ddd;padding:10px 12px}
.card h5{font-family:"PT Serif",Georgia,serif;font-weight:400;font-size:19px;line-height:20px;color:#111}
.card .type{font-family:"PT Serif",Georgia,serif;font-size:14px;color:#333}
.card .discount{position:absolute;right:14px;top:10px;text-align:center;font-weight:700;line-height:20px}
.card .discount b{display:block;color:#ff1a1a;font-size:19px}
.card .discount span{font-size:21px;color:#000;text-shadow:0 0 2px #fff}
.card .photo{margin-top:9px;width:342px;height:235px;border:1px solid #ccc;background:radial-gradient(circle at 50% 50%,#6e7078 0%,#a5a7ad 45%,#fff 70%)}
.card .note{margin-top:10px;font-size:11px;line-height:16px;color:#111}
</style>
</head>
<body>

<h1 class="abs site-title">Детский интернет-магазин, детские товары,<br>одежда для детей</h1>

<div class="abs brand"><i class="brand-dot"></i><span class="brand-name">Lira Beko</span></div>

<nav class="abs top-nav">
  <a href="#"><svg viewBox="0 0 20 20"><path d="M10 2 1 10h3v8h4v-5h4v5h4v-8h3z" fill="#c8101a"/></svg>Главная</a>
  <a href="#"><svg viewBox="0 0 20 20"><path d="M1 3h3l2 9h10l2-7H6" fill="none" stroke="#c8101a" stroke-width="2"/><circle cx="8" cy="16" r="2" fill="#c8101a"/><circle cx="15" cy="16" r="2" fill="#c8101a"/></svg>Корзина</a>
  <a href="#"><svg viewBox="0 0 20 20"><circle cx="10" cy="6" r="4.5" fill="#c8101a"/><path d="M2 19c0-5 4-7 8-7s8 2 8 7z" fill="#c8101a"/></svg>Мой аккаунт</a>
  <a href="#"><svg viewBox="0 0 20 20" fill="#c8101a"><rect x="1" y="2" width="3" height="3"/><rect x="6" y="2" width="13" height="3"/><rect x="1" y="8.5" width="3" height="3"/><rect x="6" y="8.5" width="13" height="3"/><rect x="1" y="15" width="3" height="3"/><rect x="6" y="15" width="13" height="3"/></svg>Лист подарков</a>
  <a href="#"><svg viewBox="0 0 20 20"><circle cx="10" cy="10" r="9" fill="#c8101a"/><rect x="8.7" y="8" width="2.6" height="7" fill="#fff"/><circle cx="10" cy="5.3" r="1.5" fill="#fff"/></svg>Помощь</a>
</nav>

<div class="abs auth"><span>Вход</span><span>|</span><span>Регистрация</span></div>
<div class="abs messenger"><i></i>lirabeko</div>
<div class="abs contacts">8-800-555-01-23 (Россия)<br>+7 (495) - 555-01-23 (Москва)<br>Время работы:09.00 – 18.00</div>

<div class="abs cart-line"><b>Корзина:</b> 999 &nbsp;<b>товаров</b> 99 999.99 <b>руб</b></div>
<div class="abs buy-btn">КУПИТЬ &nbsp;»</div>
<div class="abs search">Поиск<svg viewBox="0 0 25 25"><circle cx="15" cy="10" r="7" fill="none" stroke="#555" stroke-width="2.5"/><path d="M10 15 3 22" stroke="#555" stroke-width="3"/></svg></div>

<nav class="abs main-menu">
  <a href="#">Материнство</a><a href="#">Одежда</a><a href="#">Обувь</a><a href="#">Гигиена</a><a href="#">Кормление</a><a href="#">Детская<br>комната</a><a href="#">Игрушки</a><a href="#">Вне дома</a><a href="#">Праздники и<br>подарки</a><a href="#" style="padding:12px 14px 0">Текстильные<br>принадлежности</a><a href="#">Скидки и<br>акции</a><a href="#" style="border:none">Путешествия</a>
</nav>
<svg class="abs menu-flaps" viewBox="0 0 1170 12"><path d="M0 0h12v12z M1170 0h-12v12z" fill="#8e0a10"/></svg>

<div class="abs content"></div>

<div class="abs banner">
  <div class="banner-photo" role="img" aria-label="Фото: мама с ребёнком среди полевых цветов летом"></div>
  <div class="banner-headline"><div class="hot">Amazing</div><div class="sub">Summer collection</div></div>
  <div class="banner-btns"><span>see all</span><span>shop now</span></div>
</div>

<div class="abs sticker" style="top:352px;height:120px">
  <h3>5% OFF</h3>
  <p class="big">FIRST ORDER</p>
  <p class="link">Click Here for Details ····›</p>
</div>
<div class="abs sticker" style="top:481px;height:137px">
  <h3>FREE COUPON</h3>
  <p>For X Rubles for every<br>1000 Rubles spent online</p>
  <p class="link">Click Here for Details ····›</p>
</div>

<div class="abs subscribe"><div class="subscribe-inner">
  <h4>ПРИСОЕДИНЯЙТЕСЬ К НАМ</h4>
  <div class="field">Enter your email id</div>
  <div class="btn">Subscribe</div>
</div></div>

<div class="abs dots"><i class="on"></i><i></i><i></i><i></i><i></i></div>

<div class="abs card" style="left:35px">
  <h5>Vento Pushchair</h5><div class="type">Travel System</div>
  <div class="discount"><b>50%</b><span>Discount</span></div>
  <div class="photo" role="img" aria-label="Фото товара: трёхколёсная прогулочная коляска серого цвета"></div>
  <p class="note">includes pushcair, infant car seat and Cradleway<br>Weathershield</p>
</div>
<div class="abs card" style="left:415px">
  <h5>Vento Pushchair</h5><div class="type">Travel System</div>
  <div class="discount"><b>50%</b><span>Discount</span></div>
  <div class="photo" role="img" aria-label="Фото товара: трёхколёсная прогулочная коляска серого цвета"></div>
  <p class="note">includes pushcair, infant car seat and Cradleway<br>Weathershield</p>
</div>
<div class="abs card" style="left:795px">
  <h5>Vento Pushchair</h5><div class="type">Travel System</div>
  <div class="discount"><b>50%</b><span>Discount</span></div>
  <div class="photo" role="img" aria-label="Фото товара: трёхколёсная прогулочная коляска серого цвета"></div>
  <p class="note">includes pushcair, infant car seat and Cradleway<br>Weathershield</p>
</div>

</body>
</html>
```